Business Card Design: Pregnancy and Parenting Education/Support

My company is called Marigale and the tagline is Nurturing Your Growing Family. I'm based in Greater Boston and work with families from pregnancy up until 6 months old, supporting them with baby gift registry and gear consultations, postpartum doula services (in-home newborn and family care), new mom support groups for first-time and second-time moms, and various parenting and gear workshops. I also have an informational blog.

I am selling myself as my business: it's just me! I am looking for designs that convey my professional expertise in the field (I have broad experience) as well as my warm, passionate, caring, empathic, and nurturing demeanor. I want to invoke feelings of trust, serenity, collaboration, and stability, and I want to be able to reach parents of any gender and family type, as well as businesses. I want to be that blend of professional and trusted friend.

I'd like to see green (I like the green on my website! www.marigalekinship.com) to go along with the seedling image.

The pic I attached is horrible, but I really like the image of Marigale in a simple, easily readable and transferrable logo.
Updates

Incorporation of a simple, readable logo that inspires nurturing, community, trust, and kindness; and imagery not only of seedlings but of tending/nurturing seedlings, would be awesome!

Target Market(s)

Expectant/new families: men and women ages 20-40, middle class. Also, other business owners, large and small, in pregnancy and parenting-related field

Industry/Entity Type

Baby

Contact Information for Business Card

Marigale, Nurturing Your Growing Family, Dorothea Pellman, Owner/Founder, www.marigalekinship.com, dpellman@marigalekinship.com, 617-555-0148, Serving Greater Boston (If there's space/it makes sense: @MarigalebyDP, Facebook.com/MarigaleKinship)

Requirements
Nice to have
• I like circles, and I like the imagery of nurturing seedlings that comes from my business name and tagline (Marigale: Nurturing Your Growing Family). The horrible graphic attached is sort of an idea I have, but it might be too literal or too complicated to turn into a good, easily readable, easily transferrable logo? (Woman with arms around seedlings of different sizes, maybe roots going down?)

Also nice to have is twitter handle and Facebook name, but if it looks crowded, no worries! @MarigalebyDP, facebook.com/MarigaleKinship

```html
<!DOCTYPE html>
<html lang="en">
<head>
<meta charset="utf-8">
<title>Marigale – Business Card</title>
<link rel="stylesheet" href="https://fonts.googleapis.com/css2?family=Lato:wght@300;400;700;900&display=swap">
<style>
  :root {
    --backdrop: #5e5e5e;
    --card: #ffffff;
    --green: #2ebd7b;
    --ink: #2b2b2b;
    --ink-soft: #3a3a3a;
    --art-light: #eef6ef;
    --art-mid: #cfe8d4;
  }
  * { box-sizing: border-box; margin: 0; padding: 0; }
  html, body {
    width: 1200px;
    height: 900px;
    overflow: hidden;
    background: var(--backdrop);
    font-family: "Lato", Arial, sans-serif;
  }
  .stage {
    width: 1200px;
    height: 900px;
    display: flex;
    align-items: center;
    justify-content: center;
  }
  .card {
    position: relative;
    width: 1000px;
    height: 572px;
    background: var(--card);
    overflow: hidden;
    box-shadow: 0 18px 40px rgba(0, 0, 0, 0.35);
  }
  .brand {
    position: absolute;
    left: 56px;
    top: 48px;
  }
  .brand-name {
    color: var(--green);
    font-weight: 900;
    font-size: 48px;
    letter-spacing: 3px;
    line-height: 1;
    text-transform: uppercase;
  }
  .brand-tagline {
    margin-top: 10px;
    color: var(--ink);
    font-weight: 700;
    font-size: 21px;
    letter-spacing: 0.5px;
    text-transform: uppercase;
  }
  .brand-art {
    position: absolute;
    left: 70px;
    top: 175px;
    width: 210px;
    height: 250px;
    border-radius: 48% 48% 40% 40%;
    background: radial-gradient(circle at 55% 65%, var(--art-mid), var(--art-light) 70%);
  }
  .person {
    position: absolute;
    right: 60px;
    top: 160px;
    text-align: right;
  }
  .person-name {
    color: var(--ink);
    font-size: 38px;
    line-height: 1.1;
  }
  .person-name .first { font-weight: 400; }
  .person-name .last { font-weight: 700; }
  .person-role {
    margin-top: 8px;
    color: var(--green);
    font-size: 21px;
    font-weight: 400;
    letter-spacing: 3px;
    text-transform: uppercase;
  }
  .contact {
    position: absolute;
    right: 60px;
    top: 282px;
    list-style: none;
    text-align: right;
    font-size: 21px;
    line-height: 38px;
    color: var(--ink-soft);
  }
  .contact .label {
    color: var(--green);
    font-weight: 700;
  }
  .service-band {
    position: absolute;
    left: 0;
    bottom: 0;
    width: 100%;
    height: 84px;
    background: var(--green);
    display: flex;
    align-items: center;
    padding-left: 64px;
  }
  .service-area {
    color: #ffffff;
    font-size: 29px;
    font-weight: 700;
    letter-spacing: 13px;
    text-transform: uppercase;
  }
</style>
</head>
<body>
  <main class="stage">
    <article class="card">
      <header class="brand">
        <h1 class="brand-name">Marigale</h1>
        <p class="brand-tagline">Nurturing Your Growing Family</p>
      </header>

      <div class="brand-art" role="img" aria-label="Line illustration of a parent cradling green seedlings"></div>

      <section class="person">
        <h2 class="person-name"><span class="first">Dorothea</span> <span class="last">Pellman</span></h2>
        <p class="person-role">Owner/Founder</p>
      </section>

      <ul class="contact">
        <li><span class="label">phone:</span> 617-555-0148</li>
        <li><span class="label">web:</span> www.marigalekinship.com</li>
        <li><span class="label">email:</span> dpellman@marigalekinship.com</li>
        <li><span class="label">facebook:</span> Facebook.com/MarigaleKinship</li>
      </ul>

      <footer class="service-band">
        <p class="service-area">Serving Greater Boston</p>
      </footer>
    </article>
  </main>
</body>
</html>
```